Business Card Revision

Need to redesign my business cards for a new professional look. We are a courier company. You can go to www.qvrunners.com to see what we do. The trucks have an old company name (Sprout) on them but that is the company we are just now
changing the name.

Target Market(s)

Potential clients. We service the automotive, plumbing, printing, air freight industries as well as many others.

Industry/Entity Type

Business

Contact Information for Business Card

QVmotion
20864 Lark Fenmore Parkway
Marbleton, Vt 45873

Thomas R. Wendall
President

tom@qvrunners.com

Main: (470) 555-0147

```html
<!DOCTYPE html>
<html lang="en">
<head>
<meta charset="utf-8">
<title>QVmotion Business Card</title>
<link href="https://fonts.googleapis.com/css2?family=Open+Sans:wght@300;400;700;800&display=swap" rel="stylesheet">
<style>
  :root {
    --page: #e9e7e3;
    --blue-light: #1d8fd6;
    --blue: #0f72bd;
    --blue-deep: #0b5e9e;
    --green: #3fba4f;
    --green-deep: #2ea23f;
    --white: #ffffff;
    --soft-white: rgba(255, 255, 255, 0.82);
  }
  * { margin: 0; padding: 0; box-sizing: border-box; }
  html, body {
    width: 1200px;
    height: 1022px;
    overflow: hidden;
    background: var(--page);
    font-family: "Open Sans", Arial, sans-serif;
  }
  .sheet {
    width: 1200px;
    height: 1022px;
    display: flex;
    flex-direction: column;
    align-items: center;
    justify-content: center;
    gap: 40px;
  }
  .card {
    position: relative;
    width: 770px;
    height: 440px;
    border-radius: 6px;
    overflow: hidden;
    background: linear-gradient(150deg, var(--blue-light) 0%, var(--blue) 55%, var(--blue-deep) 100%);
    box-shadow: 0 6px 18px rgba(0, 0, 0, 0.18);
    color: var(--white);
  }
  .card__shape {
    position: absolute;
    inset: 0;
    width: 100%;
    height: 100%;
  }
  .wordmark {
    position: absolute;
    left: 40px;
    top: 30px;
    font-size: 96px;
    font-weight: 800;
    letter-spacing: 2px;
    text-transform: uppercase;
    line-height: 1;
    white-space: nowrap;
    color: var(--white);
  }
  .holder {
    position: absolute;
    left: 44px;
    top: 170px;
  }
  .holder__name {
    font-size: 30px;
    font-weight: 700;
    line-height: 1.2;
  }
  .holder__title {
    font-size: 19px;
    font-weight: 300;
    color: var(--soft-white);
    margin-top: 2px;
  }
  .contact {
    position: absolute;
    left: 390px;
    top: 272px;
    list-style: none;
    font-size: 17px;
    font-weight: 400;
    line-height: 28px;
    white-space: nowrap;
  }
  .contact__item {
    display: flex;
    align-items: center;
    gap: 9px;
  }
  .contact__icon {
    width: 14px;
    height: 14px;
    flex: none;
  }
  .back-name {
    position: absolute;
    right: 36px;
    top: 176px;
    font-size: 80px;
    font-weight: 800;
    letter-spacing: 2px;
    text-transform: uppercase;
    line-height: 1;
    white-space: nowrap;
    color: var(--white);
  }
</style>
</head>
<body>
<main class="sheet">

  <section class="card card--front" aria-label="Business card front">
    <svg class="card__shape" viewBox="0 0 770 440" aria-hidden="true">
      <polygon points="360,250 770,250 770,440 320,440" fill="var(--green)"/>
      <polygon points="320,440 360,250 368,250 330,440" fill="var(--green-deep)"/>
    </svg>
    <div class="wordmark">QVmotion</div>
    <div class="holder">
      <p class="holder__name">Thomas R. Wendall</p>
      <p class="holder__title">President</p>
    </div>
    <ul class="contact">
      <li class="contact__item">20864 Lark Fenmore Parkway</li>
      <li class="contact__item">Marbleton, Vt 45873</li>
      <li class="contact__item">
        <svg class="contact__icon" viewBox="0 0 14 14" aria-hidden="true">
          <path d="M3 1 L5 1 L6 4 L4.5 5.2 C5.3 7 6.8 8.6 8.8 9.5 L10 8 L13 9 L13 11.5 C13 12.4 12.3 13 11.4 13 C5.7 12.6 1.4 8.3 1 2.6 C1 1.7 1.8 1 3 1 Z" fill="var(--white)"/>
        </svg>
        (470) 555-0147
      </li>
      <li class="contact__item">
        <svg class="contact__icon" viewBox="0 0 14 14" aria-hidden="true">
          <rect x="1" y="3" width="12" height="9" rx="1" fill="none" stroke="var(--white)" stroke-width="1.5"/>
          <polyline points="1.5,3.8 7,8 12.5,3.8" fill="none" stroke="var(--white)" stroke-width="1.5"/>
        </svg>
        tom@qvrunners.com
      </li>
      <li class="contact__item">
        <svg class="contact__icon" viewBox="0 0 14 14" aria-hidden="true">
          <circle cx="7" cy="7" r="6" fill="none" stroke="var(--white)" stroke-width="1.3"/>
          <ellipse cx="7" cy="7" rx="2.6" ry="6" fill="none" stroke="var(--white)" stroke-width="1.1"/>
          <line x1="1" y1="7" x2="13" y2="7" stroke="var(--white)" stroke-width="1.1"/>
        </svg>
        www.qvrunners.com
      </li>
    </ul>
  </section>

  <section class="card card--back" aria-label="Business card back">
    <svg class="card__shape" viewBox="0 0 770 440" aria-hidden="true">
      <polygon points="0,0 170,0 90,440 0,440" fill="var(--green)"/>
      <polygon points="170,0 182,0 102,440 90,440" fill="var(--white)" opacity="0.9"/>
    </svg>
    <div class="back-name">QVmotion</div>
  </section>

</main>
</body>
</html>
```